Maplerise Trading Inc. needs an innovative idea for letterhead and visiting cards.

Maplerise Trading Inc. is a Canadian brand since 2007. It is a renown dealer of kids and office furniture locally. Moreover, exporting electric fixtures e.g. switches, LED's, down-lights etc. to Middle East and Africa. We have initiated a number of steps including re-branding, to boost our export in 2020. We have successfully designed our new logo a few months ago through 'Artfolio' and now we are looking for an innovative idea for a letterhead.
Some key points:
• Red, black and white are the three colors used in all our packaging and furniture. (grey is optional)
• Shouldn’t be too wide.
• Use of watermark is preferable.
• You can visit our North American site at www.mapleriseinc.com. Export website of the company will be launched soon. www.mapleriseinc.ca
• Same letterhead will be used locally and internationally.
• Our new logo and sample packaging is attached.

```html
<!DOCTYPE html>
<html lang="en">
<head>
<meta charset="utf-8">
<title>Maplerise Trading Inc. — Letterhead</title>
<link href="https://fonts.googleapis.com/css2?family=Roboto:wght@400;500&display=swap" rel="stylesheet">
<style>
  :root {
    --brand-red: #9b0a10;
    --ink: #1f1f1f;
    --charcoal: #4a4a4c;
    --wordmark-grey: #4d4d4f;
    --watermark: #f7eeee;
    --paper: #ffffff;
  }
  html, body {
    margin: 0;
    padding: 0;
    overflow: hidden;
    background: var(--paper);
  }
  .letterhead {
    position: relative;
    width: 848px;
    height: 1200px;
    overflow: hidden;
    background: var(--paper);
    font-family: "Roboto", Arial, sans-serif;
  }
  .brand {
    position: absolute;
    left: 60px;
    top: 56px;
    display: flex;
    align-items: center;
    gap: 12px;
  }
  .brand-square {
    width: 54px;
    height: 54px;
    border-radius: 8px;
    background: var(--brand-red);
  }
  .brand-name {
    font-weight: 400;
    font-size: 27px;
    line-height: 28px;
    letter-spacing: 0.5px;
    color: var(--wordmark-grey);
    text-transform: uppercase;
  }
  .contact {
    position: absolute;
    left: 554px;
    top: 56px;
    margin: 0;
    font-style: normal;
    font-size: 13px;
    line-height: 15px;
    color: var(--ink);
  }
  .contact span { display: block; }
  .watermark {
    position: absolute;
    left: 259px;
    top: 399px;
    width: 404px;
    height: 402px;
  }
  .footer {
    position: absolute;
    left: 0;
    bottom: 0;
    width: 848px;
    height: 43px;
    display: flex;
  }
  .footer-band {
    flex: 0 0 710px;
    background: var(--brand-red);
    display: flex;
    align-items: center;
    justify-content: center;
    color: var(--paper);
    font-size: 15px;
    letter-spacing: 0.3px;
  }
  .footer-band span { margin-left: 8px; }
  .footer-tab {
    flex: 1;
    background: var(--charcoal);
  }
</style>
</head>
<body>
  <main class="letterhead">
    <header>
      <div class="brand">
        <div class="brand-square"></div>
        <div class="brand-name">Maplerise<br>Trading</div>
      </div>
      <address class="contact">
        <span>245 Alder Crest Rd, Unit 308, Maple Grove</span>
        <span>Phone: +1 (888) 555-0142</span>
        <span>Email: sales@mapleriseinc.com</span>
      </address>
    </header>

    <svg class="watermark" viewBox="0 0 404 402" aria-hidden="true">
      <rect x="9" y="9" width="386" height="384" rx="34" fill="none" stroke="var(--watermark)" stroke-width="18"/>
      <text x="202" y="196" text-anchor="middle" font-family="Roboto, Arial, sans-serif" font-size="44" fill="var(--watermark)">MAPLERISE</text>
      <text x="202" y="248" text-anchor="middle" font-family="Roboto, Arial, sans-serif" font-size="44" fill="var(--watermark)">TRADING</text>
    </svg>

    <footer class="footer">
      <div class="footer-band"><span>www.mapleriseinc.ca</span></div>
      <div class="footer-tab"></div>
    </footer>
  </main>
</body>
</html>
```